Flyer Design Project

We need a flyer design for a 1 year old domestic cleaning company based in Wiltshire, England. We provide households with high quality, hard working cleaners. We would like to see designs which use blue (the colour on the logo attatched). The final design should communicate a clean, premier and thorough service in a clear and bold way. We would like the flyer to be A5 with a single sided design. We have attached an A5 word document with the words we would like to be used in the design, what we need is for you to give it some life, colour, artwork and a professional touch. We are perfectionsists which we would like to illustrate to our customer through this flyer.
Updates

payment has been guaranteed!

Sorry..... please no pictures of females on the designs. many thanks

Target Market(s)

females with higher than average income, aged 30-50. Have families and work 9-5.

Industry/Entity Type

It Company

Requirements
Must have
• The flyer must include the logo attatched and the words in the A5 document attatched. With RELIABLE CLEANERS preferably the headline. A5 - single sided.
The Flyer must also include our introductory offer.....
First Clean FREE
Allow us to demonstrate our standards

this should be emphasised.

PLEASE NOTE: can this be added to the list of words on the flyer please:

Ironing service - one day turn around
Nice to have
• some pictures - nothing cheesey. Again, pictures should communicate our modern professional approach.

```html
<!DOCTYPE html>
<html lang="en">
<head>
<meta charset="utf-8">
<title>Brookmere Cleaners – Flyer</title>
<link rel="stylesheet" href="https://fonts.googleapis.com/css2?family=Bree+Serif&family=Roboto+Condensed:wght@700&family=Mulish:wght@700;800&family=Open+Sans:wght@400;600&display=swap">
<style>
  :root {
    --brand-blue: #1d64b0;
    --brand-blue-dark: #173a73;
    --brand-cyan: #2aa6e0;
    --accent-red: #e8363b;
    --paper: #f3f5f7;
    --ink: #1a1a1a;
    --white: #ffffff;
    --photo-light: #efe9df;
    --photo-mid: #d8c8b2;
    --photo-dark: #8d6f52;
  }
  * { margin: 0; padding: 0; box-sizing: border-box; }
  html, body { width: 846px; height: 1200px; overflow: hidden; background: var(--paper); }
  .flyer {
    position: relative;
    width: 846px;
    height: 1200px;
    overflow: hidden;
    background: var(--paper);
    font-family: "Mulish", sans-serif;
  }
  .shapes { position: absolute; inset: 0; width: 846px; height: 1200px; }

  .headline {
    position: absolute;
    top: 66px; left: 0; width: 846px;
    text-align: center;
    font-family: "Bree Serif", serif;
    font-size: 74px;
    letter-spacing: 1px;
    word-spacing: 28px;
    color: var(--accent-red);
    -webkit-text-stroke: 3px var(--white);
    paint-order: stroke fill;
    text-shadow: 0 2px 3px rgba(0,0,0,0.25);
  }

  .hero-photo {
    position: absolute;
    top: 210px; left: 0;
    width: 846px; height: 430px;
    background: linear-gradient(100deg, var(--photo-light) 0%, #f6f2ec 35%, var(--photo-mid) 70%, var(--photo-dark) 100%);
  }

  .brand {
    position: absolute;
    top: 236px; left: 44px;
    display: flex; align-items: center; gap: 16px;
  }
  .brand-mark {
    width: 84px; height: 84px; border-radius: 50%;
    background: var(--brand-blue);
  }
  .brand-name {
    font-family: "Open Sans", sans-serif;
    font-weight: 600;
    font-size: 38px;
    color: var(--brand-blue-dark);
  }
  .brand-tagline {
    position: absolute;
    top: 340px; left: 124px;
    font-family: "Open Sans", sans-serif;
    font-weight: 600;
    font-size: 20px;
    color: var(--brand-blue-dark);
  }

  .offer {
    position: absolute;
    top: 580px; left: -10px;
    width: 732px; height: 128px;
    background: var(--brand-blue);
    border: 5px solid var(--white);
    border-radius: 0 22px 22px 0;
    display: flex; align-items: center;
    padding-left: 48px;
    font-family: "Bree Serif", serif;
    font-size: 80px;
    color: var(--white);
  }
  .offer-free {
    margin-left: 18px;
    color: var(--accent-red);
    background: var(--white);
    padding: 0 10px;
    line-height: 90px;
    border-radius: 4px;
    letter-spacing: 2px;
  }

  .offer-sub {
    position: absolute;
    top: 730px; left: 0; width: 846px;
    text-align: center;
    font-family: "Roboto Condensed", sans-serif;
    font-weight: 700;
    font-size: 33px;
    color: var(--accent-red);
  }

  .services {
    position: absolute;
    top: 784px; left: 46px;
    list-style: none;
  }
  .services li {
    font-weight: 800;
    font-size: 22px;
    line-height: 29px;
    color: var(--ink);
  }
  .services li::before {
    content: "•";
    color: var(--accent-red);
    margin-right: 6px;
  }

  .contact-email {
    position: absolute;
    top: 966px; left: 350px;
    width: 476px;
    text-align: center;
    font-weight: 800;
    font-size: 25px;
    line-height: 36px;
    color: var(--white);
  }

  .contact-phone {
    position: absolute;
    top: 1070px; left: 0; width: 846px;
    text-align: center;
    font-family: "Bree Serif", serif;
    font-size: 68px;
    letter-spacing: 2px;
    word-spacing: 26px;
    color: var(--accent-red);
    -webkit-text-stroke: 3px var(--white);
    paint-order: stroke fill;
  }
</style>
</head>
<body>
<main class="flyer">
  <svg class="shapes" viewBox="0 0 846 1200" aria-hidden="true">
    <defs>
      <linearGradient id="footer-fill" x1="0" y1="0" x2="0" y2="1">
        <stop offset="0" stop-color="#2068b5"/>
        <stop offset="1" stop-color="#163468"/>
      </linearGradient>
    </defs>
    <path class="top-swoosh" d="M230 0 H846 V40 C640 18 430 10 230 0 Z" fill="var(--brand-blue)"/>
    <path d="M360 0 H846 V18 C680 8 520 4 360 0 Z" fill="var(--brand-cyan)"/>
    <rect class="header-band" x="0" y="186" width="846" height="24" fill="var(--brand-blue)"/>
    <rect class="offer-band" x="700" y="634" width="146" height="30" fill="var(--brand-blue)"/>
    <polygon class="footer-edge" points="0,1082 846,800 846,836 0,1108" fill="var(--brand-cyan)"/>
    <polygon class="footer-panel" points="0,1106 846,834 846,1200 0,1200" fill="url(#footer-fill)"/>
  </svg>

  <h1 class="headline">Reliable Cleaners!</h1>

  <div class="hero-photo" role="img" aria-label="Photo of a bright, tidy modern living room with a white sofa and wooden floor"></div>

  <div class="brand">
    <span class="brand-mark"></span>
    <span class="brand-name">Brookmere Cleaners</span>
  </div>
  <p class="brand-tagline">Premier Domestic Cleaners</p>

  <h2 class="offer">First Clean <span class="offer-free">FREE</span></h2>

  <p class="offer-sub">Allow Us To Demonstrate Our Standards......</p>

  <ul class="services">
    <li>Ironing Service - One Day Turn Around</li>
    <li>Personalised Service</li>
    <li>Constantly Thorough</li>
    <li>Hassel Free</li>
    <li>Insured</li>
    <li>Regular Weekly Cleans</li>
    <li>No Contracts</li>
  </ul>

  <p class="contact-email">Email:<br>brookmerecleaners@example.co.uk</p>

  <p class="contact-phone">Tele: 07700900461</p>
</main>
</body>
</html>
```